Redesign Application Page for Job Position

Would like to get a redesign on our Job Application Page.
You can use brennoxguard or valmoreta as references.

http://www.careersatklv.example/KLV/NCreateAccount.aspx?aga=qwtrzx4hemLK7

Target Market(s)

Professional Security Individuals

Industry/Entity Type

Security Guard

Coding

Coded - Design and coding required

Number of Pages Required

1 page

Font styles to use
Sans Serif

Colors
0255a3
3276b5
ffcf3e
fee18a

Requirements
Must have
• User Friendly, Easy Navigation. Must be very easy to read and understand what is required or missing.
Should not have
• Ugly or Bulky

```html
<!DOCTYPE html>
<html lang="en">
<head>
<meta charset="utf-8">
<title>KLV Application Form</title>
<link href="https://fonts.googleapis.com/css2?family=Open+Sans:wght@400;600;700&display=swap" rel="stylesheet">
<style>
:root{
  --page-bg:#eef2f7;
  --white:#ffffff;
  --brand-blue:#0255a3;
  --brand-blue-mid:#3276b5;
  --brand-yellow:#ffcf3e;
  --brand-yellow-soft:#fee18a;
  --row-stripe:#2a6aac;
  --text:#1f2a37;
  --muted:#8a94a0;
  --border:#c9d4e2;
  --footer-bg:#023f7a;
  --footer-text:#c9d8ea;
}
*{box-sizing:border-box;margin:0;padding:0}
html,body{width:721px;height:1200px;overflow:hidden}
body{background:var(--page-bg);font-family:"Open Sans",Arial,sans-serif;color:var(--text);position:relative}
.site-header{position:absolute;left:0;top:0;width:721px;height:74px;background:var(--white);border-bottom:3px solid var(--brand-yellow)}
.brand{position:absolute;left:28px;top:20px;display:flex;align-items:center;gap:8px}
.brand-dot{width:34px;height:34px;border-radius:50%;background:var(--brand-blue)}
.brand-name{font-size:8px;font-weight:700;color:var(--brand-blue);letter-spacing:.2px}
.hotline{position:absolute;right:11px;top:29px;display:flex;align-items:center;gap:4px;font-size:14px;font-weight:600;color:var(--brand-blue)}
.card{position:absolute;left:95px;top:100px;width:530px;height:988px;background:var(--white);border-top:4px solid var(--brand-blue);box-shadow:0 6px 14px rgba(2,85,163,.18)}
.card > *{position:absolute}
.title{left:0;width:100%;top:13px;text-align:center;font-size:17.5px;font-weight:600;color:var(--brand-blue)}
.subtitle{left:0;width:100%;top:46px;text-align:center;font-size:11.5px}
.divider{left:11px;width:508px;top:68px;border-top:2px solid var(--brand-yellow-soft)}
.label{font-size:8px;font-weight:600;color:var(--text)}
.field{height:20px;border:1px solid var(--border);border-radius:3px;background:var(--white);font-size:8px;color:var(--muted);padding:0 7px;display:flex;align-items:center}
.select{justify-content:space-between;color:#4a5562}
.select::after{content:"▾";font-size:8px;color:var(--brand-blue)}
.radio{display:inline-block;width:7px;height:7px;border:1px solid var(--brand-blue-mid);border-radius:50%;margin:0 3px;vertical-align:middle;background:var(--white)}
.section-heading{font-size:12.5px;font-weight:600;color:var(--brand-blue);padding-left:7px;border-left:3px solid var(--brand-yellow);line-height:14px}
.data-table{border-collapse:collapse;background:var(--brand-blue-mid);color:var(--white);font-size:8px}
.data-table th{text-align:left;font-weight:700;height:26px;padding-left:6px;background:var(--brand-blue);border-bottom:2px solid var(--brand-yellow)}
.data-table td{padding-left:6px}
.data-table tbody tr:nth-child(odd){background:var(--row-stripe)}
.license-table tbody td{height:34.5px}
.table-input{height:20px;background:var(--white);border-radius:3px;font-size:8px;color:#4a5562;padding:0 7px;display:flex;align-items:center}
.shift-table tbody td{height:26px}
.tick{display:inline-block;width:7px;height:7px;background:var(--white);border-radius:1px}
.check-list{list-style:none;font-size:8px;left:19px;top:688px}
.check-list li{height:13px;display:flex;align-items:center;gap:5px}
.check-box{width:8px;height:8px;border:1px solid var(--brand-blue-mid);background:var(--white);border-radius:2px}
.btn{height:22px;top:941px;font-size:8.5px;font-weight:600;border-radius:3px;display:flex;align-items:center;justify-content:center}
.btn-primary{background:var(--brand-blue);color:var(--white)}
.btn-secondary{background:var(--brand-yellow);color:var(--brand-blue)}
.site-footer{position:absolute;left:0;top:1114px;width:721px;height:86px;background:var(--footer-bg);border-top:3px solid var(--brand-yellow);text-align:center;font-size:8px;color:var(--footer-text);padding-top:19px;line-height:13px}
.site-footer strong{color:var(--brand-yellow);font-weight:600}
</style>
</head>
<body>
<header class="site-header">
  <div class="brand"><span class="brand-dot"></span><span class="brand-name">KELVANE GUARD SERVICES, INC.</span></div>
  <div class="hotline">
    <svg width="10" height="15" viewBox="0 0 10 15"><rect x="1" y="1" width="8" height="13" rx="1.5" fill="#0255a3"/><rect x="2.5" y="3" width="5" height="7" fill="#fee18a"/></svg>
    1-800-555-0148
  </div>
</header>

<main class="card">
  <h1 class="title">Application Form</h1>
  <p class="subtitle">Complete all required fields, then click "Continue" to create your account!</p>
  <div class="divider"></div>

  <span class="label" style="left:11px;top:81px">First name</span>
  <span class="label" style="left:182px;top:81px">Second name</span>
  <span class="label" style="left:353px;top:81px">Last name</span>
  <div class="field" style="left:11px;top:97px;width:166px">First name</div>
  <div class="field" style="left:182px;top:97px;width:165px">Middle name</div>
  <div class="field" style="left:353px;top:97px;width:165px">Last name</div>

  <span class="label" style="left:11px;top:127px">Gender:</span>
  <span class="label" style="left:11px;top:145px;font-weight:400">Male<span class="radio"></span>Female<span class="radio"></span></span>
  <span class="label" style="left:97px;top:127px">Date Of Birth</span>
  <div class="field" style="left:97px;top:142px;width:250px;height:21px;color:#4a5562">mm/dd/yyyy</div>

  <span class="label" style="left:11px;top:173px">Address</span>
  <div class="field" style="left:11px;top:189px;width:508px">1234 Main St</div>
  <span class="label" style="left:11px;top:219px">Address 2</span>
  <div class="field" style="left:11px;top:234px;width:508px">Apartment, studio, or floor</div>

  <span class="label" style="left:11px;top:265px">City</span>
  <span class="label" style="left:268px;top:265px">State</span>
  <span class="label" style="left:353px;top:265px">Nearest office</span>
  <span class="label" style="left:439px;top:265px">Zip</span>
  <div class="field" style="left:11px;top:280px;width:250px"></div>
  <div class="field select" style="left:268px;top:280px;width:79px">Choose...</div>
  <div class="field select" style="left:353px;top:280px;width:80px">Choose...</div>
  <div class="field" style="left:439px;top:280px;width:79px"></div>

  <span class="label" style="left:11px;top:310px">Mobile number</span>
  <span class="label" style="left:268px;top:310px">Phone number</span>
  <div class="field" style="left:11px;top:326px;width:250px"></div>
  <div class="field" style="left:268px;top:326px;width:250px"></div>

  <span class="label" style="left:11px;top:356px">Job position</span>
  <div class="field select" style="left:11px;top:371px;width:508px">Choose...</div>

  <span class="label" style="left:19px;top:401px">SSN</span>
  <div class="field" style="left:19px;top:417px;width:69px"></div>

  <h2 class="section-heading" style="left:11px;top:449px">License Details</h2>
  <table class="data-table license-table" style="left:11px;top:474px;width:508px">
    <thead><tr><th style="width:98px">Type</th><th style="width:206px">Number</th><th>Expire Date</th></tr></thead>
    <tbody>
      <tr><td style="vertical-align:top;padding-top:8px">Guard Card</td><td><div class="table-input" style="width:129px"></div></td><td><div class="table-input" style="width:95px">mm/dd/yyyy</div></td></tr>
      <tr><td style="vertical-align:top;padding-top:8px">Baton</td><td><div class="table-input" style="width:129px"></div></td><td><div class="table-input" style="width:95px">mm/dd/yyyy</div></td></tr>
      <tr><td style="vertical-align:top;padding-top:8px">Gun Permit</td><td><div class="table-input" style="width:129px"></div></td><td><div class="table-input" style="width:95px">mm/dd/yyyy</div></td></tr>
    </tbody>
  </table>

  <span class="label" style="left:11px;top:613px">ID Document Type</span>
  <span class="label" style="left:142px;top:613px">ID Document Number</span>
  <span class="label" style="left:317px;top:613px">ID Document Expiry Date</span>
  <div class="field select" style="left:11px;top:629px;width:114px">Choose...</div>
  <div class="field" style="left:142px;top:629px;width:158px"></div>
  <div class="field select" style="left:317px;top:629px;width:114px">Choose...</div>

  <h2 class="section-heading" style="left:11px;top:662px">Additional Languages</h2>
  <ul class="check-list">
    <li><span class="check-box"></span>Spanish</li>
    <li><span class="check-box"></span>French</li>
    <li><span class="check-box"></span>Japanese</li>
    <li><span class="check-box"></span>Chinese</li>
  </ul>

  <span class="label" style="left:11px;top:746px">Email</span>
  <span class="label" style="left:268px;top:746px">How did you hear about us?</span>
  <div class="field" style="left:11px;top:762px;width:250px">Email</div>
  <div class="field select" style="left:268px;top:762px;width:165px">Choose...</div>

  <h2 class="section-heading" style="left:11px;top:794px">Work Availability:</h2>
  <table class="data-table shift-table" style="left:11px;top:818px;width:508px">
    <thead><tr><th style="width:111px">Shift</th><th style="width:57px">Sun</th><th style="width:64px">Mon</th><th style="width:55px">Tue</th><th style="width:63px">Wed</th><th style="width:62px">Thu</th><th style="width:48px">Fri</th><th>Sat</th></tr></thead>
    <tbody>
      <tr><td>Day Shift</td><td><span class="tick"></span></td><td><span class="tick"></span></td><td><span class="tick"></span></td><td><span class="tick"></span></td><td><span class="tick"></span></td><td><span class="tick"></span></td><td><span class="tick"></span></td></tr>
      <tr><td>Swing Shift</td><td><span class="tick"></span></td><td><span class="tick"></span></td><td><span class="tick"></span></td><td><span class="tick"></span></td><td><span class="tick"></span></td><td><span class="tick"></span></td><td><span class="tick"></span></td></tr>
      <tr><td>Night Shift</td><td><span class="tick"></span></td><td><span class="tick"></span></td><td><span class="tick"></span></td><td><span class="tick"></span></td><td><span class="tick"></span></td><td><span class="tick"></span></td><td><span class="tick"></span></td></tr>
    </tbody>
  </table>

  <div class="btn btn-primary" style="left:214px;width:53px">Continue</div>
  <div class="btn btn-secondary" style="left:271px;width:47px">Discard</div>
</main>

<footer class="site-footer">
  <strong>Need Help?</strong><br>
  Call us at: (310)555-0192<br>
  and ask for Human Resource Representative.
</footer>
</body>
</html>
```